Website Design Project for Beauty & Wellness Professionals

As background information, I have a website that is focused on Beauty & Wellness Professionals:
- Job Search (www.trilhavelora.com)
- Business Classifieds (negocios.trilhavelora.com)
- Freelancer Classifieds (freelancer.trilhavelora.com)
- Course Reviews (cursos.trilhavelora.com)

All those websites use standard templates.

I need a DESIGN for the HOME PAGE (no coding) of the Website Platform that consolidates the four platforms under the same design.

Website designs that we like:
- nestorly.com
- workpane.com

Target Market(s)

Brazilian Professionals from Beauty & Wellness sector

Industry/Entity Type

Business

Requirements
Must have
• Website designs that we like:
- nestorly.com
- workpane.com

```html
<!DOCTYPE html>
<html lang="en">
<head>
<meta charset="utf-8">
<title>Trilha Velora – Home</title>
<link href="https://fonts.googleapis.com/css2?family=Arimo:wght@400;700&family=Open+Sans:wght@400;600;700&display=swap" rel="stylesheet">
<style>
:root{
  --coral:#f47c5a;
  --coral-dark:#e8694a;
  --sky:#9fd7e9;
  --sky-dark:#7fc6dd;
  --leaf:#7cc576;
  --ink:#222;
  --muted:#555;
  --grey-band:#ececec;
  --line:#d6d6d6;
  --white:#fff;
}
*{box-sizing:border-box;margin:0;padding:0}
html,body{width:690px;height:1200px;overflow:hidden;background:var(--white)}
body{font-family:"Open Sans",Arial,sans-serif;color:var(--ink)}
.page{position:relative;width:690px;height:1200px;overflow:hidden}
.abs{position:absolute}

/* top bar */
.topbar{left:0;top:0;width:690px;height:16px;background:var(--coral);color:var(--white);font-size:7px;font-weight:600;text-align:right;padding:3px 20px 0 0}
.topbar span{margin-left:6px}

/* header */
.header{left:0;top:16px;width:690px;height:40px;background:var(--white)}
.brand{position:absolute;left:89px;top:9px;display:flex;align-items:center;gap:6px;font-family:"Arimo",Arial,sans-serif;font-size:17px;color:var(--coral)}
.brand i{display:block;width:22px;height:22px;border-radius:50%;background:var(--coral)}
.nav{position:absolute;left:255px;top:0;height:40px;display:flex}
.nav a{display:flex;align-items:center;justify-content:center;height:40px;border-left:1px solid #e3e3e3;font-size:8.5px;font-weight:600;color:var(--ink);text-decoration:none}
.nav a:last-child{border-right:1px solid #e3e3e3}
.nav .active{color:var(--coral)}
.nav .caret{display:inline-block;margin-left:4px;border:3px solid transparent;border-top:4px solid var(--ink);margin-top:4px}

/* hero */
.hero{left:0;top:56px;width:690px;height:189px;background:
  radial-gradient(circle at 18% 40%,rgba(240,120,180,.55),transparent 22%),
  radial-gradient(circle at 80% 55%,rgba(230,80,50,.6),transparent 20%),
  radial-gradient(circle at 55% 70%,rgba(255,200,120,.35),transparent 25%),
  linear-gradient(180deg,#3b2a28 0%,#5a3a35 55%,#2c2020 100%)}
.hero-title{left:0;top:102px;width:690px;text-align:center;font-family:"Arimo",Arial,sans-serif;font-weight:700;font-size:24px;color:var(--white)}
.hero-sub{left:0;top:131px;width:690px;text-align:center;font-family:"Arimo",Arial,sans-serif;font-size:15px;color:#f0e6e6}
.search{left:89px;top:167px;width:510px;height:25px}
.search-label{position:absolute;left:0;top:0;width:78px;height:25px;background:#e9e2dc;font-size:8px;font-weight:700;display:flex;align-items:center;justify-content:center}
.search-input{position:absolute;left:81px;top:2px;width:178px;height:21px;background:var(--white);border:1px solid #ccc;font-size:7px;color:#999;padding:6px 5px}
.search-select{position:absolute;left:264px;top:2px;width:177px;height:21px;background:var(--white);border:1px solid #ccc;font-size:7px;color:#999;padding:6px 5px}
.search-select b{position:absolute;right:0;top:0;width:17px;height:19px;background:#555}
.search-select b:after{content:"";position:absolute;left:5px;top:8px;border:4px solid transparent;border-top:5px solid var(--white)}
.search-btn{position:absolute;left:445px;top:2px;width:61px;height:21px;background:var(--leaf);color:var(--white);font-size:9px;font-weight:700;display:flex;align-items:center;justify-content:center}

/* trends + news */
.trends-head{left:89px;top:245px;width:252px;height:44px;background:var(--leaf);color:var(--white);padding:6px 10px}
.trends-head h2{font-family:"Arimo",Arial,sans-serif;font-size:14px;font-weight:700}
.trends-head p{font-size:8.5px}
.trends-photo{left:89px;top:289px;width:252px;height:123px;background:linear-gradient(135deg,#d9d9d9,#9a9a9a 60%,#e4e4e4)}
.news-tab{left:343px;top:245px;width:77px;height:20px;background:var(--coral);color:var(--white);font-family:"Arimo",Arial,sans-serif;font-size:11px;font-weight:700;padding:3px 7px}
.news-tab:after{content:"";position:absolute;left:24px;bottom:-5px;border:5px solid transparent;border-top:5px solid var(--coral);border-bottom:0}
.news-line{left:353px;top:273px;font-size:6.5px;color:var(--muted)}
.news-dots{left:576px;top:276px;display:flex;gap:2px}
.news-dots i{width:5px;height:5px;border-radius:50%;border:1px solid #888}
.news-dots i:first-child{background:var(--coral);border-color:var(--coral)}
.news-item{left:341px;width:260px;height:59px;background:var(--sky)}
.news-photo{position:absolute;left:0;top:0;width:58px;height:100%;background:linear-gradient(160deg,#6b5a52,#b9a79d)}
.news-body{position:absolute;left:68px;top:5px;right:6px;color:var(--white)}
.news-body h3{font-size:6.5px;font-weight:700}
.news-body p{font-size:5px;line-height:1.35;margin-top:2px}
.tags{display:flex;gap:5px;margin-top:5px}
.tags span{background:var(--sky-dark);font-size:5px;padding:2px 5px}

/* services */
.section-title{left:0;width:690px;text-align:center;font-family:"Arimo",Arial,sans-serif;font-weight:700;font-size:22px;color:var(--ink)}
.section-sub{left:0;width:690px;text-align:center;font-family:"Arimo",Arial,sans-serif;font-size:13px;color:var(--muted)}
.card{top:479px;width:116px;height:195px;border-radius:58px;background:var(--sky);color:var(--white);text-align:center;padding:12px 10px 0}
.card.is-featured{background:var(--coral)}
.card-icon{width:96px;height:96px;margin:0 auto;border-radius:50%;background:var(--white);display:flex;align-items:center;justify-content:center}
.card h3{font-family:"Arimo",Arial,sans-serif;font-size:10px;font-weight:700;margin-top:10px}
.card p{font-size:6px;line-height:1.35;margin-top:5px}

/* gallery */
.gallery{left:0;top:699px;width:690px;height:327px;background:var(--grey-band)}
.gallery-rule{left:89px;top:768px;width:512px;height:1px;background:var(--line)}
.gallery-mark{left:338px;top:762px;width:13px;height:13px;border-radius:50%;background:var(--coral)}
.hexes{left:0;top:786px}

/* footer */
.footer{left:0;top:1026px;width:690px;height:150px;background:var(--coral);color:var(--white);text-align:center}
.social{left:0;top:1005px;width:690px;display:flex;justify-content:center;gap:5px}
.social i{display:block;width:46px;height:46px;border-radius:50%;background:var(--coral);border:3px solid var(--white)}
.foot-block h4{font-size:7px;font-weight:700;margin-bottom:3px}
.foot-block p{font-size:5.5px;line-height:1.6}
.copyright{left:0;top:1183px;width:690px;text-align:center;font-size:6px;color:var(--muted)}
</style>
</head>
<body>
<div class="page">

  <div class="abs topbar"><span>Welcome, visitor!</span><span>|</span><span>Register</span><span>|</span><span>Login</span></div>

  <header class="abs header">
    <div class="brand"><i></i>Trilha Velora</div>
    <nav class="nav">
      <a class="active" style="width:42px">Home</a>
      <a style="width:107px">Categories of Business<span class="caret"></span></a>
      <a style="width:79px">For Professionals</a>
      <a style="width:63px">For Business</a>
      <a style="width:54px">About Us</a>
    </nav>
  </header>

  <section class="abs hero" role="img" aria-label="Blurred photo of a busy beauty salon interior with warm lights"></section>
  <h1 class="abs hero-title">Neque porro quisquam est qui dolorem</h1>
  <p class="abs hero-sub">Neque porro quisquam est qui dolorem ipsum quia</p>
  <div class="abs search">
    <div class="search-label">Local Job Search</div>
    <div class="search-input">Ex: Manicure São Paulo, Rio de Janeiro Hairdresser</div>
    <div class="search-select">All categories<b></b></div>
    <div class="search-btn">SEARCH</div>
  </div>

  <div class="abs trends-head"><h2>Trilha Velora trends</h2><p>Neque porro quisquam est qui dolorem ipsum quia</p></div>
  <div class="abs trends-photo" role="img" aria-label="Black and white fashion photo of a model seated in a studio"></div>

  <div class="abs news-tab">Latest news</div>
  <p class="abs news-line">Lorem ipsum dolor sit neque porro quisquam est qui ipsum</p>
  <div class="abs news-dots"><i></i><i></i><i></i></div>

  <article class="abs news-item" style="top:289px">
    <div class="news-photo" role="img" aria-label="Portrait photo of a salon professional"></div>
    <div class="news-body">
      <h3>Renata Moraes Lins - São Paulo</h3>
      <p>Salon reception work, March 2009 period. Assistant hairdresser role, hair care support since October 2009.</p>
      <div class="tags"><span>Manicure &amp; Pedicure</span><span>renata lins</span><span>07/22/2013</span></div>
    </div>
  </article>
  <article class="abs news-item" style="top:351px">
    <div class="news-photo" role="img" aria-label="Portrait photo of a salon professional"></div>
    <div class="news-body">
      <h3>Célia Prado Nunes - Manicure / Pedicure</h3>
      <p>Nail studio work, April 2010 period. Senior manicure role, pedicure care support since August 2011.</p>
      <div class="tags"><span>Manicure &amp; Pedicure</span><span>célia prado</span><span>07/22/2013</span></div>
    </div>
  </article>

  <h2 class="abs section-title" style="top:421px">Neque porro quisquam est qui dolorem</h2>
  <p class="abs section-sub" style="top:448px">Neque porro quisquam est qui dolorem ipsum quia</p>

  <div class="abs card is-featured" style="left:90px">
    <div class="card-icon"><svg width="60" height="60" viewBox="0 0 60 60"><circle cx="30" cy="20" r="13" fill="var(--coral)"/><path d="M6 56c0-14 11-22 24-22s24 8 24 22z" fill="var(--coral)"/></svg></div>
    <h3>Job Search</h3>
    <p>Nemo enim ipsam voluptatem quia voluptas sit aspernatur aut odit aut fugit, sed quia consequuntur magni dolores eos qui ratione voluptatem.</p>
  </div>
  <div class="abs card" style="left:222px">
    <div class="card-icon"><svg width="60" height="60" viewBox="0 0 60 60" fill="var(--sky)"><rect x="8" y="22" width="30" height="30"/><rect x="42" y="6" width="9" height="9" transform="rotate(45 46 10)"/><rect x="38" y="20" width="8" height="8" transform="rotate(45 42 24)"/><rect x="48" y="22" width="7" height="7" transform="rotate(45 51 25)"/><path d="M18 22v30M28 22v30M8 32h30M8 42h30" stroke="var(--white)" stroke-width="1.5"/></svg></div>
    <h3>Business Classifieds</h3>
    <p>Nemo enim ipsam voluptatem quia voluptas sit aspernatur aut odit aut fugit, sed quia consequuntur magni dolores eos qui ratione voluptatem.</p>
  </div>
  <div class="abs card" style="left:353px">
    <div class="card-icon"><svg width="60" height="60" viewBox="0 0 60 60"><path d="M14 6h26l10 10v38H14z" fill="var(--sky)"/><path d="M16 46l24-24 5 5-24 24h-5z" fill="var(--white)"/><path d="M19 45l20-20" stroke="var(--sky)" stroke-width="3"/></svg></div>
    <h3>Freelancer Classifieds</h3>
    <p>Nemo enim ipsam voluptatem quia voluptas sit aspernatur aut odit aut fugit, sed quia consequuntur magni dolores eos qui ratione voluptatem.</p>
  </div>
  <div class="abs card" style="left:485px">
    <div class="card-icon"><svg width="60" height="60" viewBox="0 0 60 60" fill="none" stroke="var(--sky)" stroke-width="5"><rect x="8" y="8" width="44" height="44"/><path d="M8 30h44M30 8v44"/><rect x="20" y="20" width="20" height="20" fill="var(--white)"/></svg></div>
    <h3>Course Reviews</h3>
    <p>Nemo enim ipsam voluptatem quia voluptas sit aspernatur aut odit aut fugit, sed quia consequuntur magni dolores eos qui ratione voluptatem.</p>
  </div>

  <section class="abs gallery"></section>
  <h2 class="abs section-title" style="top:715px">Our Trilha Velora gallery</h2>
  <p class="abs section-sub" style="top:743px">Neque porro quisquam est qui dolorem ipsum quia</p>
  <div class="abs gallery-rule"></div>
  <div class="abs gallery-mark"></div>

  <svg class="abs hexes" width="690" height="200" viewBox="0 0 690 200" role="img" aria-label="Honeycomb gallery of black and white beauty portrait photos">
    <defs>
      <linearGradient id="tone-a" x1="0" y1="0" x2="1" y2="1"><stop offset="0" stop-color="#e2e2e2"/><stop offset="1" stop-color="#7a7a7a"/></linearGradient>
      <linearGradient id="tone-b" x1="1" y1="0" x2="0" y2="1"><stop offset="0" stop-color="#3a3a3a"/><stop offset="1" stop-color="#bdbdbd"/></linearGradient>
      <linearGradient id="tone-warm" x1="0" y1="0" x2="1" y2="1"><stop offset="0" stop-color="#f2d2b5"/><stop offset="1" stop-color="#c98d68"/></linearGradient>
      <polygon id="hex" points="50,0 100,28 100,84 50,112 0,84 0,28"/>
    </defs>
    <use href="#hex" x="40" y="0" fill="url(#tone-a)"/>
    <use href="#hex" x="142" y="0" fill="url(#tone-b)"/>
    <use href="#hex" x="244" y="0" fill="url(#tone-a)"/>
    <use href="#hex" x="346" y="0" fill="url(#tone-b)"/>
    <use href="#hex" x="448" y="0" fill="url(#tone-a)"/>
    <use href="#hex" x="550" y="0" fill="url(#tone-b)"/>
    <use href="#hex" x="-12" y="86" fill="url(#tone-b)"/>
    <use href="#hex" x="91" y="86" fill="url(#tone-a)"/>
    <use href="#hex" x="193" y="86" fill="url(#tone-warm)" stroke="var(--coral)" stroke-width="5"/>
    <use href="#hex" x="295" y="86" fill="url(#tone-b)"/>
    <use href="#hex" x="397" y="86" fill="url(#tone-a)"/>
    <use href="#hex" x="499" y="86" fill="url(#tone-b)"/>
    <use href="#hex" x="601" y="86" fill="url(#tone-a)"/>
  </svg>

  <footer class="abs footer">
    <div class="foot-block" style="margin-top:38px"><h4>JOB VACANCIES</h4><p>LEARN with Online Courses &nbsp;|&nbsp; Increase your chances of EMPLOYMENT &nbsp;|&nbsp; Salon Owner? Advertise Job Vacancies &nbsp;|&nbsp; Latest JOBS Job!</p></div>
    <div class="foot-block" style="margin-top:8px"><h4>PROFESSIONALS</h4><p>Renata Moraes Lins - São Paulo &nbsp;|&nbsp; Célia Prado Nunes - Manicure / Pedicure &nbsp;|&nbsp; Marta Quintela - Eyebrow Designer - Osasco &nbsp;|&nbsp; ISADORA LEMKE - Stage Aesthetics - São Paulo<br>Helena Duarte Vieira - makeup artist - Rio de Janeiro</p></div>
    <div class="foot-block" style="margin-top:8px"><h4>BEAUTY CAREER</h4><p>LEARN with Online Courses &nbsp;|&nbsp; Increase your chances of EMPLOYMENT &nbsp;|&nbsp; Salon Owner? Advertise Job Vacancies &nbsp;|&nbsp; Latest JOBS Job!</p></div>
  </footer>
  <div class="abs social"><i></i><i></i><i></i><i></i></div>
  <p class="abs copyright">© 2013 Trilha Velora Carreiras. All rights reserved</p>

</div>
</body>
</html>
```